Home page makeover

Take my existing home page, www.maplecrestledger.com and redesign layout to look more current considering today's touch design prevalence.
Reuse existing elements or suggest improved ones if available.
I generally have average CSS and HTML skills using div containers, defining lists and using columns to create the code to support the layout.
Updates
Just wanted to send out a quick message to thank all of you for your submissions. Many of you offered nice designs, but unfortunately could only choose one.
Target Market(s)
Generally targeting individuals with some assets for retirement. Basically your average working professional or business owner.
Industry/Entity Type
It Support
Look and feel
Each slider illustrates characteristics of the customer's brand and the style your logo design should communicate.

```html
<!DOCTYPE html>
<html lang="en">
<head>
<meta charset="utf-8">
<title>Maplecrest Ledger – Home</title>
<link rel="stylesheet" href="https://fonts.googleapis.com/css2?family=Open+Sans:wght@400;600;700&family=Roboto+Condensed:wght@400;700&display=swap">
<style>
  :root {
    --green-dark: #0b4f12;
    --green-band: #2a6e1c;
    --green-text: #1f6b1a;
    --green-bright: #5db41c;
    --lime: #8cc63f;
    --blue-price: #1a7fc0;
    --text-body: #555;
    --rule: #dedede;
    --white: #fff;
  }
  * { box-sizing: border-box; margin: 0; padding: 0; }
  html, body { width: 753px; height: 1200px; overflow: hidden; }
  body { position: relative; background: var(--white); font-family: "Open Sans", sans-serif; color: var(--text-body); }
  .abs { position: absolute; }

  /* header */
  .site-header { position: absolute; left: 0; top: 0; width: 753px; height: 72px;
    background: linear-gradient(#fff, #e4e4e4); border-bottom: 1px solid #ccc; }
  .brand { position: absolute; left: 88px; top: 18px; display: flex; align-items: center; gap: 8px;
    font-family: "Roboto Condensed", sans-serif; font-weight: 700; font-size: 26px; color: var(--green-text); }
  .brand-mark { width: 20px; height: 20px; background: var(--green-text); }
  .main-nav { position: absolute; top: 20px; left: 341px; display: flex; gap: 0; font-family: "Roboto Condensed", sans-serif; font-size: 15px; color: #111; }
  .main-nav a { position: absolute; top: 5px; color: #111; text-decoration: none; white-space: nowrap; }
  .nav-btn { position: absolute; top: 0 !important; height: 25px; border: 2px solid var(--green-bright); border-radius: 4px;
    color: var(--green-text) !important; display: flex; align-items: center; justify-content: center; background: #fff; }

  /* hero */
  .hero-panel { position: absolute; top: 72px; height: 244px; }
  .hero-band { position: absolute; top: 137px; height: 50px; background: rgba(255,255,255,.72);
    font-family: "Roboto Condensed", sans-serif; font-weight: 700; font-size: 40px; color: var(--green-text);
    display: flex; align-items: center; justify-content: center; letter-spacing: -0.5px; }

  /* welcome */
  .welcome-band { position: absolute; left: 0; top: 316px; width: 753px; height: 76px; background: var(--green-band); }
  .welcome-title { position: absolute; left: 89px; top: 336px; color: #fff; font-weight: 700; font-size: 18px; line-height: 19px; }
  .mission { position: absolute; left: 88px; top: 411px; width: 240px; font-size: 10.6px; line-height: 14.7px; }
  .mission a { color: var(--green-text); text-decoration: none; }
  .video-frame { position: absolute; left: 348px; top: 327px; width: 317px; height: 225px; background: #d0d0d0; padding: 5px; }
  .video-player { position: relative; width: 100%; height: 100%; background: #000; }
  .video-title { position: absolute; left: 8px; top: 5px; font-size: 8px; color: #ddd; }
  .video-still { position: absolute; left: 38px; top: 20px; width: 230px; height: 172px;
    background: linear-gradient(135deg, #e9e9e9, #8a8a8a 60%, #333); }
  .play-btn { position: absolute; left: 134px; top: 90px; width: 48px; height: 34px; background: rgba(20,20,20,.85); border-radius: 8px; }
  .video-controls { position: absolute; left: 0; bottom: 0; width: 100%; height: 18px; background: #1b1b1b; border-top: 2px solid #444; font-size: 7px; color: #ccc; }

  /* features */
  .section-title { position: absolute; left: 88px; font-weight: 700; font-size: 17px; color: var(--green-text); }
  .rule { position: absolute; left: 88px; width: 577px; background: var(--rule); }
  .feature { position: absolute; top: 612px; font-size: 10.6px; line-height: 14.6px; }
  .feature-divider { position: absolute; top: 601px; width: 1px; height: 171px; background: var(--rule); }

  /* pricing */
  .signup-cta { position: absolute; left: 99px; top: 795px; width: 177px; height: 59px; border-radius: 3px;
    background: linear-gradient(#6fce1c, #3a8a10); color: #fff; font-family: "Roboto Condensed", sans-serif;
    font-size: 31px; display: flex; align-items: center; justify-content: center; }
  .price-box { position: absolute; top: 795px; width: 177px; height: 59px; border-radius: 3px;
    background: linear-gradient(#f2f2f2, #d9d9d9); padding: 4px 12px; font-family: "Roboto Condensed", sans-serif; }
  .price-amount { font-weight: 700; font-size: 30px; line-height: 32px; color: var(--blue-price); letter-spacing: -0.5px; }
  .price-note { font-size: 12px; line-height: 13px; color: #333; }

  /* testimonials */
  .quote-card { position: absolute; top: 930px; height: 67px; border: 2px solid #e2e2e2; border-radius: 5px;
    box-shadow: 0 1px 3px rgba(0,0,0,.15); padding: 14px 14px; background: #fff; }
  .quote-text { font-size: 10px; line-height: 13px; color: #444; }
  .quote-author { font-size: 8px; font-weight: 700; color: #222; margin-top: 1px; }
  .clip { position: absolute; right: 6px; top: -6px; }

  /* footer */
  .site-footer { position: absolute; left: 0; top: 1025px; width: 753px; height: 175px; background: var(--green-dark); border-top: 2px solid #063a0b; }
  .footer-brand { position: absolute; left: 128px; top: 1066px; display: flex; align-items: center; gap: 8px;
    font-family: "Roboto Condensed", sans-serif; font-weight: 700; font-size: 26px; color: #fff; }
  .footer-brand .brand-mark { background: #fff; }
  .keep-title { position: absolute; left: 303px; top: 1048px; color: #fff; font-size: 17px; font-weight: 600; }
  .contact-email { position: absolute; left: 303px; top: 1077px; color: #fff; font-size: 12px; font-weight: 600; }
  .subscribe-input { position: absolute; left: 304px; top: 1101px; width: 153px; height: 22px; background: #fff;
    font-size: 9px; color: #555; padding: 5px 7px; }
  .subscribe-btn { position: absolute; left: 457px; top: 1101px; width: 53px; height: 22px; background: var(--lime);
    font-size: 10px; font-weight: 600; color: #0b3a0b; display: flex; align-items: center; justify-content: center; }
  .social { position: absolute; top: 1130px; width: 27px; height: 27px; border-radius: 50%; background: #fff; }
  .copyright { position: absolute; left: 305px; top: 1176px; font-size: 7.5px; letter-spacing: 1px; color: var(--lime); }
</style>
</head>
<body>

<header class="site-header">
  <div class="brand"><span class="brand-mark"></span>Maplecrest</div>
  <nav class="main-nav">
    <a style="left:0">HOME</a>
    <a style="left:52px">ABOUT</a>
    <a style="left:109px">CONTACT</a>
    <a class="nav-btn" style="left:171px;width:63px">SIGN IN</a>
    <a class="nav-btn" style="left:240px;width:63px">SIGN UP</a>
  </nav>
</header>

<div class="hero-panel" style="left:0;width:250px;background:linear-gradient(135deg,#dcdccf,#9fa39a 60%,#e8e8e2)" role="img" aria-label="Banknotes, pen and financial statements"></div>
<div class="hero-panel" style="left:251px;width:251px;background:linear-gradient(160deg,#ffffff,#c9c9c9 55%,#5a5a5a)" role="img" aria-label="Reading glasses resting on a laptop keyboard"></div>
<div class="hero-panel" style="left:503px;width:250px;background:linear-gradient(#b9d3ea,#e2eaf0 45%,#c8b79a 65%,#8f8a6e)" role="img" aria-label="Rope hammock on a porch"></div>
<div class="hero-band" style="left:0;width:250px">INDENTIFY</div>
<div class="hero-band" style="left:251px;width:251px">PLAN</div>
<div class="hero-band" style="left:503px;width:250px">RETIRE</div>

<div class="welcome-band"></div>
<h1 class="welcome-title">Welcome to<br>Maplecrest Ledger</h1>
<p class="mission">Our mission is to help you make the basic determination of when and how you can retire. This site will provide the average individual a comprehensive tool to assist with managing this daunting proposition and help you identify a realistic age that you can retire given your expectations and needs during retirement considering all of your available resources. <a href="#">Read more</a></p>

<div class="video-frame">
  <div class="video-player">
    <span class="video-title">Demo.wmv</span>
    <div class="video-still" role="img" aria-label="Video still of glasses on a laptop with the word Plan"></div>
    <div class="play-btn">
      <svg width="48" height="34" viewBox="0 0 48 34"><path d="M19 10 L31 17 L19 24 Z" fill="#fff"/></svg>
    </div>
    <div class="video-controls"><span style="position:absolute;left:50px;top:3px">0:00 / 0:28</span></div>
  </div>
</div>

<h2 class="section-title" style="top:570px">Features</h2>
<div class="rule" style="top:598px;height:2px"></div>
<p class="feature" style="left:89px;width:128px">Identify and project your retirement needs and expectations including basic living expenses, housing costs, recreation, big ticket non-recurring items, medical and nursing home care.</p>
<div class="feature-divider" style="left:225px"></div>
<p class="feature" style="left:240px;width:128px">Identify and project all your sources of retirement income including retirement savings, other savings, pension plans, Social Security, life insurance and working part-time during retirement for a period of time.</p>
<div class="feature-divider" style="left:375px"></div>
<p class="feature" style="left:393px;width:126px">Strategize tapping into the equity of your real estate including swapping your primary residence for a different home or retirement area, or selling and renting.</p>
<div class="feature-divider" style="left:529px"></div>
<p class="feature" style="left:545px;width:118px">Produce easy to understand results featuring the Readiness Gauge™.<br><br>Save your work so you can return, revisit and edit your retirement plan at a later date.</p>
<div class="rule" style="top:772px;height:1px"></div>

<a class="signup-cta">SIGN UP</a>
<div class="price-box" style="left:288px"><div class="price-amount">ONLY $19.99</div><div class="price-note">FOR A ONE YEAR MEMBERSHIP</div></div>
<div class="price-box" style="left:476px"><div class="price-amount">ONLY $9.99</div><div class="price-note">PER YEAR AFTER THAT</div></div>
<div class="rule" style="top:875px;height:1px"></div>

<h2 class="section-title" style="top:892px">Testimonial</h2>
<div class="quote-card" style="left:88px;width:273px">
  <p class="quote-text">“This site is a great place to get a handle on your retirement strategy”</p>
  <p class="quote-author">Owen, New Jersey</p>
  <svg class="clip" width="22" height="22" viewBox="0 0 22 22"><path d="M6 17 L15 6 a3 3 0 0 1 4 4 L10 20 a2 2 0 0 1 -3 -3 L15 9" fill="none" stroke="#1fa3c9" stroke-width="2"/></svg>
</div>
<div class="quote-card" style="left:382px;width:283px">
  <p class="quote-text">“It's the only retirement projection tool for the average user that puts it all together”</p>
  <p class="quote-author">Paul, New York</p>
  <svg class="clip" width="22" height="22" viewBox="0 0 22 22"><path d="M6 17 L15 6 a3 3 0 0 1 4 4 L10 20 a2 2 0 0 1 -3 -3 L15 9" fill="none" stroke="#1fa3c9" stroke-width="2"/></svg>
</div>

<footer class="site-footer"></footer>
<div class="footer-brand"><span class="brand-mark"></span>Maplecrest</div>
<h3 class="keep-title">Keep in touch.</h3>
<p class="contact-email">contact@maplecrestledger.com</p>
<div class="subscribe-input">Enter your email address</div>
<div class="subscribe-btn">SUBMIT</div>
<span class="social" style="left:304px" aria-label="Social link"></span>
<span class="social" style="left:335px" aria-label="Social link"></span>
<p class="copyright">© 2013 COPYRIGHT MAPLECREST LEDGER, INC. ALL RIGHTS RESERVED.</p>

</body>
</html>
```